Memento Mori Calendar

I’m looking for a graphic designer to create a Memento Mori–style life calendar that captures the essence of QUILNEXA — minimal, timeless, and deeply philosophical.

The design should be black and white only, with a refined, clean aesthetic and a sense of stillness and precision.
It should feel modern yet eternal, reflecting the themes of time, mortality, and presence.

Deliverables (Print-Ready Files):

24 x 30 in

24 x 32 in

24 x 36 in

A1 (594 x 841 mm)

All formats should be high-resolution and ready for professional printing (300 DPI, CMYK).

Design Requirements:

The calendar layout should follow the Memento Mori life calendar concept (weeks of life represented as small squares or circles).

The overall tone: minimal, meditative, monochrome.

Include the brand name: QUILNEXA (in an elegant, understated placement).

Add the following quote at the bottom or in a subtle position:

“Life can only be understood backwards; but it must be lived forwards.”
— Anselm Brodtvik

Target Market(s)

The QUILNEXA audience consists of urban, creative individuals aged 25 to 45, belonging to a middle to upper-middle income class. They lead conscious, quietly ambitious lives, seeking balance between inner depth and modern design. Their values center on awareness, presence, authenticity, and emotional depth, reflected in their preference for a monochrome, minimal, and timeless aesthetic. They tend to be introverted, reflective, and spiritually curious, drawn to brands that embody meaning and restraint rather than excess. Their cultural and stylistic affinities include Vinth, Polde, Ro Sefi, The Garden of Hours, Dussant, and Varolé — labels that share QUILNEXAs devotion to simplicity, substance, and subtle ritual.

Font styles to use
Serif
Sans Serif

Colors

Designer to choose only greyscale colors for use in the design.

Requirements
Must have
• The calendar layout should follow the Memento Mori life calendar concept (weeks of life represented as small squares or circles). The overall tone: minimal, meditative, monochrome. Include the brand name: trvolquen (in an elegant, understated placement). Add the following quote at the bottom or in a subtle position: “Life can only be understood backwards; but it must be lived forwards.” — Anselm Brodtvik

```html
<!DOCTYPE html>
<html lang="en">
<head>
<meta charset="utf-8">
<title>Memento Mori Life Calendar — QUILNEXA</title>
<link rel="stylesheet" href="https://fonts.googleapis.com/css2?family=Montserrat:wght@400;500;600;700&family=Tinos:ital,wght@1,700&display=swap">
<style>
  :root {
    --backdrop: #d9d9d9;
    --paper: #ffffff;
    --ink: #000000;
    --ink-soft: #4a4a4a;
    --cell-line: #5a5a5a;
    --mist-light: #f1f1f1;
    --mist-mid: #bdbdbd;
    --mist-dark: #2b2b2b;
  }
  html, body {
    margin: 0;
    width: 1006px;
    height: 1200px;
    overflow: hidden;
    background: var(--backdrop);
  }
  .poster {
    position: absolute;
    left: 23px;
    top: 0;
    width: 960px;
    height: 1200px;
    display: block;
  }
  .sheet { fill: var(--paper); }
  .title { font-family: "Montserrat", sans-serif; font-weight: 600; fill: var(--ink); }
  .brand { font-family: "Montserrat", sans-serif; font-weight: 400; fill: var(--ink-soft); }
  .axis-label { font-family: "Montserrat", sans-serif; font-weight: 700; font-size: 17px; fill: var(--ink); }
  .week-nums text, .year-nums text { font-family: "Montserrat", sans-serif; font-weight: 700; fill: var(--ink); }
  .week-nums text { font-size: 8px; text-anchor: middle; }
  .week-nums .major { font-size: 14px; }
  .year-nums text { font-size: 8px; text-anchor: end; }
  .year-nums .major { font-size: 14px; }
  .cell { fill: var(--paper); stroke: var(--cell-line); stroke-width: 1.1; }
  .panel { fill: var(--paper); }
  .quote { font-family: "Tinos", serif; font-style: italic; font-weight: 700; font-size: 26px; fill: var(--ink); text-anchor: end; }
</style>
</head>
<body>
<svg class="poster" viewBox="142 118 1476 1844" xmlns="http://www.w3.org/2000/svg">
  <defs>
    <pattern id="week-cell" width="19" height="18.7" patternUnits="userSpaceOnUse">
      <rect class="cell" x="0.6" y="0.6" width="10.6" height="10.6" rx="2.2"/>
    </pattern>
    <linearGradient id="figure-tone" x1="0" y1="0" x2="0.6" y2="1">
      <stop offset="0" stop-color="var(--mist-light)"/>
      <stop offset="0.6" stop-color="var(--mist-mid)"/>
      <stop offset="1" stop-color="var(--mist-dark)"/>
    </linearGradient>
    <linearGradient id="smoke-tone" x1="1" y1="0" x2="0" y2="1">
      <stop offset="0" stop-color="var(--mist-mid)"/>
      <stop offset="0.5" stop-color="var(--mist-light)"/>
      <stop offset="1" stop-color="var(--mist-mid)"/>
    </linearGradient>
  </defs>

  <rect class="sheet" x="142" y="118" width="1476" height="1844"/>

  <path d="M142 1390 H396 V1848 H700 V1962 H142 Z" fill="url(#figure-tone)" opacity="0.85" role="img" aria-label="Photograph of a cloaked figure standing on a dark rock among ink-like smoke"/>
  <rect x="1450" y="1080" width="168" height="760" fill="url(#smoke-tone)" opacity="0.8" role="img" aria-label="Monochrome ink smoke and fine cracked lines drifting at the edge"/>

  <text class="title" transform="translate(338,1300) rotate(-90)" font-size="148" textLength="1075" lengthAdjust="spacingAndGlyphs">MEMENTO MORI</text>

  <text class="brand" transform="translate(1557,735) rotate(-90)" font-size="56" textLength="405" lengthAdjust="spacing">QUILNEXA</text>

  <text class="axis-label" x="440" y="181">Week</text>
  <text class="axis-label" transform="translate(405,256) rotate(-90)">Year</text>

  <g class="week-nums">
    <text x="442.5" y="202">1</text><text x="461.5" y="202">2</text><text x="480.5" y="202">3</text><text x="499.5" y="202">4</text><text class="major" x="518.5" y="203">5</text><text x="537.5" y="202">6</text><text x="556.5" y="202">7</text><text x="575.5" y="202">8</text><text x="594.5" y="202">9</text><text class="major" x="613.5" y="203">10</text><text x="632.5" y="202">11</text><text x="651.5" y="202">12</text><text x="670.5" y="202">13</text><text x="689.5" y="202">14</text><text class="major" x="708.5" y="203">15</text><text x="727.5" y="202">16</text><text x="746.5" y="202">17</text><text x="765.5" y="202">18</text><text x="784.5" y="202">19</text><text class="major" x="803.5" y="203">20</text><text x="822.5" y="202">21</text><text x="841.5" y="202">22</text><text x="860.5" y="202">23</text><text x="879.5" y="202">24</text><text class="major" x="898.5" y="203">25</text><text x="917.5" y="202">26</text>
    <text x="953.5" y="202">27</text><text x="972.5" y="202">28</text><text x="991.5" y="202">29</text><text class="major" x="1010.5" y="203">30</text><text x="1029.5" y="202">31</text><text x="1048.5" y="202">32</text><text x="1067.5" y="202">33</text><text x="1086.5" y="202">34</text><text class="major" x="1105.5" y="203">35</text><text x="1124.5" y="202">36</text><text x="1143.5" y="202">37</text><text x="1162.5" y="202">38</text><text x="1181.5" y="202">39</text><text class="major" x="1200.5" y="203">40</text><text x="1219.5" y="202">41</text><text x="1238.5" y="202">42</text><text x="1257.5" y="202">43</text><text x="1276.5" y="202">44</text><text class="major" x="1295.5" y="203">45</text><text x="1314.5" y="202">46</text><text x="1333.5" y="202">47</text><text x="1352.5" y="202">48</text><text x="1371.5" y="202">49</text><text class="major" x="1390.5" y="203">50</text><text x="1409.5" y="202">51</text><text x="1428.5" y="202">52</text>
  </g>

  <rect class="panel" x="400" y="1433" width="1045" height="405" rx="8"/>

  <g class="week-grid">
    <g transform="translate(437,210)"><rect width="494" height="187" fill="url(#week-cell)"/><rect x="511" width="494" height="187" fill="url(#week-cell)"/></g>
    <g transform="translate(437,415)"><rect width="494" height="187" fill="url(#week-cell)"/><rect x="511" width="494" height="187" fill="url(#week-cell)"/></g>
    <g transform="translate(437,620)"><rect width="494" height="187" fill="url(#week-cell)"/><rect x="511" width="494" height="187" fill="url(#week-cell)"/></g>
    <g transform="translate(437,825)"><rect width="494" height="187" fill="url(#week-cell)"/><rect x="511" width="494" height="187" fill="url(#week-cell)"/></g>
    <g transform="translate(437,1030)"><rect width="494" height="187" fill="url(#week-cell)"/><rect x="511" width="494" height="187" fill="url(#week-cell)"/></g>
    <g transform="translate(437,1235)"><rect width="494" height="187" fill="url(#week-cell)"/><rect x="511" width="494" height="187" fill="url(#week-cell)"/></g>
    <g transform="translate(437,1440)"><rect width="494" height="187" fill="url(#week-cell)"/><rect x="511" width="494" height="187" fill="url(#week-cell)"/></g>
    <g transform="translate(437,1645)"><rect width="494" height="187" fill="url(#week-cell)"/><rect x="511" width="494" height="187" fill="url(#week-cell)"/></g>
  </g>

  <g class="year-nums">
    <g><text x="427" y="219">1</text><text x="427" y="237.7">2</text><text x="427" y="256.4">3</text><text x="427" y="275.1">4</text><text x="427" y="293.8">5</text><text x="427" y="312.5">6</text><text x="427" y="331.2">7</text><text x="427" y="349.9">8</text><text x="427" y="368.6">9</text><text class="major" x="430" y="389">10</text></g>
    <g transform="translate(0,205)"><text x="427" y="219">11</text><text x="427" y="237.7">12</text><text x="427" y="256.4">13</text><text x="427" y="275.1">14</text><text x="427" y="293.8">15</text><text x="427" y="312.5">16</text><text x="427" y="331.2">17</text><text x="427" y="349.9">18</text><text x="427" y="368.6">19</text><text class="major" x="430" y="389">20</text></g>
    <g transform="translate(0,410)"><text x="427" y="219">21</text><text x="427" y="237.7">22</text><text x="427" y="256.4">23</text><text x="427" y="275.1">24</text><text x="427" y="293.8">25</text><text x="427" y="312.5">26</text><text x="427" y="331.2">27</text><text x="427" y="349.9">28</text><text x="427" y="368.6">29</text><text class="major" x="430" y="389">30</text></g>
    <g transform="translate(0,615)"><text x="427" y="219">31</text><text x="427" y="237.7">32</text><text x="427" y="256.4">33</text><text x="427" y="275.1">34</text><text x="427" y="293.8">35</text><text x="427" y="312.5">36</text><text x="427" y="331.2">37</text><text x="427" y="349.9">38</text><text x="427" y="368.6">39</text><text class="major" x="430" y="389">40</text></g>
    <g transform="translate(0,820)"><text x="427" y="219">41</text><text x="427" y="237.7">42</text><text x="427" y="256.4">43</text><text x="427" y="275.1">44</text><text x="427" y="293.8">45</text><text x="427" y="312.5">46</text><text x="427" y="331.2">47</text><text x="427" y="349.9">48</text><text x="427" y="368.6">49</text><text class="major" x="430" y="389">50</text></g>
    <g transform="translate(0,1025)"><text x="427" y="219">51</text><text x="427" y="237.7">52</text><text x="427" y="256.4">53</text><text x="427" y="275.1">54</text><text x="427" y="293.8">55</text><text x="427" y="312.5">56</text><text x="427" y="331.2">57</text><text x="427" y="349.9">58</text><text x="427" y="368.6">59</text><text class="major" x="430" y="389">60</text></g>
    <g transform="translate(0,1230)"><text x="427" y="219">61</text><text x="427" y="237.7">62</text><text x="427" y="256.4">63</text><text x="427" y="275.1">64</text><text x="427" y="293.8">65</text><text x="427" y="312.5">66</text><text x="427" y="331.2">67</text><text x="427" y="349.9">68</text><text x="427" y="368.6">69</text><text class="major" x="430" y="389">70</text></g>
    <g transform="translate(0,1435)"><text x="427" y="219">71</text><text x="427" y="237.7">72</text><text x="427" y="256.4">73</text><text x="427" y="275.1">74</text><text x="427" y="293.8">75</text><text x="427" y="312.5">76</text><text x="427" y="331.2">77</text><text x="427" y="349.9">78</text><text x="427" y="368.6">79</text><text class="major" x="430" y="389">80</text></g>
  </g>

  <text class="quote" x="1565" y="1888">“Life can only be understood backwards; but it must be lived forwards.”</text>
  <text class="quote" x="1565" y="1921">— Anselm Brodtvik</text>
</svg>
</body>
</html>
```